Business Card Design Project

- makeup artist business card

- original and creative

- Elegant design

- Feel free to come out with cool designs but stick to being elegant and attractive

- Design relates to makeup

- includes name, occupation, contact numbers, email, website

- regular size business card

- round corner card

- double sided

- on 1 side it should just have the website name in the center " velvetbrushhue.com "

Industry/Entity Type

Business

Requirements
Must have
• Marla Tobin
Makeup Artist
USA: +1 (213)555-0147
Singapore: +65 90007312
marlatobin@velvetbrushhue.com
www.velvetbrushhue.com
Should not have
• nothing cartoon looking.
Pictures of makeup being grab from the internet.. Examples: eyes or lips.

```html
<!DOCTYPE html>
<html lang="en">
<head>
<meta charset="utf-8">
<title>Marla Tobin — Makeup Artist Business Card</title>
<link href="https://fonts.googleapis.com/css2?family=Jost:wght@300;400&display=swap" rel="stylesheet">
<style>
  :root {
    --canvas-bg: #ecebe8;
    --card-white: #f7f7f5;
    --blush: #e9a4aa;
    --blush-light: #f3cfd1;
    --blush-mid: #eeb9bd;
    --card-shadow: 0 18px 40px rgba(60, 45, 40, 0.18), 0 3px 8px rgba(60, 45, 40, 0.12);
  }
  * { box-sizing: border-box; margin: 0; padding: 0; }
  html, body {
    width: 1200px;
    height: 1200px;
    overflow: hidden;
  }
  body {
    background: var(--canvas-bg);
    font-family: "Jost", "Futura", sans-serif;
    display: flex;
    align-items: center;
    justify-content: center;
    gap: 80px;
  }
  .card {
    position: relative;
    width: 420px;
    height: 735px;
    border-radius: 10px;
    overflow: hidden;
    background: var(--card-white);
    box-shadow: var(--card-shadow);
  }

  /* Back side: wave pattern with centred website label */
  .card-back .wave-field {
    position: absolute;
    inset: 0;
    background: linear-gradient(160deg, var(--blush-light) 0%, var(--blush-mid) 55%, var(--blush-light) 100%);
  }
  .card-back .site-label {
    position: absolute;
    left: 20px;
    right: 20px;
    bottom: 28px;
    height: 52px;
    background: var(--card-white);
    border: 3px solid var(--blush);
    border-radius: 26px;
    display: flex;
    align-items: center;
    justify-content: center;
    white-space: nowrap;
    color: var(--blush);
    font-weight: 400;
    font-size: 21px;
    letter-spacing: 2px;
    text-transform: uppercase;
  }

  /* Front side: name and contact details */
  .card-front .details {
    position: absolute;
    left: 40px;
    right: 24px;
    top: 382px;
    color: var(--blush);
    font-weight: 300;
  }
  .details .name {
    font-size: 31px;
    font-weight: 300;
    letter-spacing: 1px;
    text-transform: uppercase;
    line-height: 1.1;
  }
  .details .role {
    font-size: 21px;
    margin-top: 6px;
  }
  .details .phones {
    margin-top: 68px;
    font-size: 22px;
    line-height: 36px;
  }
  .details .online {
    margin-top: 36px;
    font-size: 21px;
    line-height: 30px;
    white-space: nowrap;
  }
</style>
</head>
<body>
  <section class="card card-back" aria-label="Card back">
    <div class="wave-field" role="img" aria-label="Blush pink and white overlapping wave-scale pattern"></div>
    <div class="site-label">www.velvetbrushhue.com</div>
  </section>

  <section class="card card-front" aria-label="Card front">
    <div class="details">
      <h1 class="name">Marla Tobin</h1>
      <p class="role">Makeup Artist</p>
      <p class="phones">USA: +1 (213)555-0147<br>Singapore: +65 90007312</p>
      <p class="online">marlatobin@velvetbrushhue.com<br>www.velvetbrushhue.com</p>
    </div>
  </section>
</body>
</html>
```